B.O.G
Brenwick Orchard Group
I need double sided standard sized Business Card [3.5" x 2"]
Any fonts
Professional
Linh Tran
President
3318 Velmont Ave
Marlow Bay, CA 90417
1-800-555-0147
info@velmorik.com
www.velmorik.com
Anything

```html
<!DOCTYPE html>
<html lang="en">
<head>
<meta charset="utf-8">
<title>B.O.G Business Card</title>
<link rel="stylesheet" href="https://fonts.googleapis.com/css2?family=Arimo:wght@400;700&display=swap">
<style>
  :root {
    --page: #ffffff;
    --card-edge: #b9bcc2;
    --brand-blue: #1b47a6;
    --deep-blue: #1d3a9c;
    --bright-blue: #1f86d6;
    --brand-green: #18a548;
    --lime: #8cc63f;
    --dark-green: #0a7a34;
    --ink: #1a3f9c;
    --white: #ffffff;
  }
  * { margin: 0; padding: 0; box-sizing: border-box; }
  html, body {
    width: 1200px; height: 739px; overflow: hidden;
    background: var(--page);
    font-family: "Arimo", Arial, sans-serif;
  }
  .canvas { position: relative; width: 1200px; height: 739px; }
  .card {
    position: absolute; width: 572px; height: 329px;
    border: 1px solid var(--card-edge); overflow: hidden;
  }
  .card--front { left: 31px; top: 36px; background: var(--white); }
  .card--back { left: 616px; top: 36px; width: 550px;
    background: linear-gradient(90deg, var(--deep-blue) 0%, #1e5fbe 55%, var(--bright-blue) 100%); }
  .card--alt { left: 317px; top: 389px; width: 569px; height: 327px;
    background: linear-gradient(90deg, #000 0%, #063d1b 10%, var(--dark-green) 22%, var(--brand-green) 60%, #1cb052 100%); }
  .swoosh { position: absolute; inset: 0; width: 100%; height: 100%; }
  .brand { position: absolute; display: flex; align-items: center; gap: 10px; color: var(--brand-blue); font-weight: 700; white-space: nowrap; }
  .brand__dot { width: 46px; height: 46px; border-radius: 50%; background: var(--brand-green); flex: none; }
  .brand__mark { font-size: 44px; line-height: 1; letter-spacing: 1px; }
  .brand__name { font-size: 12px; letter-spacing: 0.5px; text-transform: uppercase; margin-top: 3px; }
  .card--front .brand { left: 22px; top: 18px; }
  .card--back .brand { left: 50%; top: 50%; transform: translate(-46%, -50%); color: var(--white); }
  .card--back .brand__dot { width: 66px; height: 66px; background: var(--white); }
  .card--back .brand__mark { font-size: 58px; }
  .card--back .brand__name { font-size: 14px; }
  .person { position: absolute; left: 34px; top: 160px; color: var(--ink); }
  .person__name { font-size: 23px; font-weight: 400; }
  .person__title { font-size: 13px; margin-top: 4px; color: #213a7a; }
  .contact {
    position: absolute; right: 22px; top: 232px; text-align: right;
    color: var(--white); font-size: 11.5px; line-height: 17px; font-style: normal;
  }
  .emblem { position: absolute; left: 50%; top: 50%; transform: translate(-50%, -50%);
    display: flex; align-items: center; gap: 14px; color: var(--white); font-weight: 700; white-space: nowrap; }
  .emblem__ring { width: 140px; height: 140px; border-radius: 50%; background: var(--white); }
  .emblem__mark { font-size: 40px; }
</style>
</head>
<body>
<main class="canvas">
  <section class="card card--front" aria-label="Card front">
    <svg class="swoosh" viewBox="0 0 572 329" preserveAspectRatio="none" aria-hidden="true">
      <defs>
        <linearGradient id="band" x1="0" y1="0" x2="1" y2="0">
          <stop offset="0" stop-color="#1e62c4"/>
          <stop offset="1" stop-color="#1d3a9c"/>
        </linearGradient>
      </defs>
      <path d="M0,329 L0,300 C190,262 400,160 572,0 L572,329 Z" fill="url(#band)"/>
      <path d="M0,292 C190,254 395,152 560,0" fill="none" stroke="var(--lime)" stroke-width="4"/>
    </svg>
    <div class="brand">
      <span class="brand__dot"></span>
      <div>
        <div class="brand__mark">B.O.G</div>
        <div class="brand__name">Brenwick Orchard Group</div>
      </div>
    </div>
    <div class="person">
      <h1 class="person__name">Linh Tran</h1>
      <p class="person__title">President</p>
    </div>
    <address class="contact">
      3318 Velmont Ave, Marlow Bay, CA 90417<br>
      Toll free: 1-800-555-0147 | Phone: 1-800-555-0147<br>
      Cell: 1-555-555-0192 | Fax: 1-800-555-0147<br>
      Email: info@velmorik.com | www.velmorik.com
    </address>
  </section>

  <section class="card card--back" aria-label="Card back">
    <div class="brand">
      <span class="brand__dot"></span>
      <div>
        <div class="brand__mark">B.O.G</div>
        <div class="brand__name">Brenwick Orchard Group</div>
      </div>
    </div>
  </section>

  <section class="card card--alt" aria-label="Alternate card back">
    <div class="emblem">
      <span class="emblem__ring"></span>
      <span class="emblem__mark">B.O.G</span>
    </div>
  </section>
</main>
</body>
</html>
```